Website: Orvalink Business Consultants, Qianhai SEZ, China

Our client is a business consultancy firm and will be the first to set up in the Qianhai Shenzhen-Hong Kong Modern Service Industry Cooperation Zone, China So we need a corporate website concept that engages service, finance and technology sector companies. The company can provide all the necessary services needed to set up shop in Qianhai. They are looking for a modern, international, reliable and strong image.

Here are some websites for reference prupose:

http://www.brenwickpartners.example/ (we like the dynamic banner and clear, clean layout of this website)

http://www.dovetrassadvisory.example/ (we like the background city image, use of light font, hover over menu functions and color scheme - purple and grey)

http://www.pelmo.example/ (we like the simplicity of this website, clear lines and we like the dynamic banner)
Updates

Hello, We are currently undecided between three logo designs.  All three have been uploaded to the design brief so that you can use them as reference for the website design. Thx

Also please take note of the addition menu selection 'About Qianhai'. Thx

Hello all Designers, First of all we want thank you for participating in our website competition, the calibre of design was high and we appreciated the expedience. Our company is Quillon Reach Web Design and Internet Marketing based in Shenzhen, China. We anticipate rapid growth in the Chinese domestic market as the country shifts in to a service sector economy. We hope to continue building reliable working relationships with you based on idea sharing and constructive feedback. Once again, Thankyou, QR Team

Target Market(s)

International finance and technology companies looking to set up in Qianhai Special Economic Zone, China

Industry/Entity Type

Finance

Requirements
Must have
• Initial design for home page and in later selection stages a secondary page will be required.

The design should be for PSD concepts only no code!

Menu bar, Photo banner -
A. Photo banner and text overlay,
B.Photo Banner and text description to left or right.

Social Connect icons, Site search bar (top right), Logo space (top left).

Menu bar at top with Home, About Us, About Qianhai, Services, Portfolio, Partners, Our Team Contact Us.

Standard 3-4 box layout - Banner at top and 2-3 boxes under banner.

Colour scheme- A. Purple and Blue, must have light background/body
B. Shades of white, black and grey.

Simple, clear, clean, sharp.

```html
<!DOCTYPE html>
<html lang="en">
<head>
<meta charset="utf-8">
<title>Orvalink Business Consultants</title>
<link rel="stylesheet" href="https://fonts.googleapis.com/css2?family=Jost:wght@300;400;500&family=Open+Sans:wght@400&display=swap">
<style>
:root{
  --white:#ffffff;
  --ink:#222222;
  --grey:#6b6b6b;
  --line:#dddddd;
  --nav-bg:#3b1236;
  --nav-active:#5c0c2e;
  --nav-text:#3fa3d8;
  --brand:#b63da6;
  --brand-sub:#555555;
  --tile-top:#2a5a7e;
  --tile-bottom:#173954;
  --tile-accent:#7ab6dc;
  --dot:#5a5a5a;
  --dot-active:#2f8fb8;
}
*{margin:0;padding:0;box-sizing:border-box}
html,body{width:1200px;height:1140px;overflow:hidden;background:var(--white)}
body{position:relative;font-family:"Jost",sans-serif;color:var(--ink)}

.site-header{position:absolute;left:0;top:0;width:1200px;height:178px;background:var(--white);border-bottom:4px solid #111}
.brand{position:absolute;left:116px;top:92px;display:flex;align-items:center;gap:14px}
.brand-mark{width:62px;height:62px;border-radius:50%;background:var(--brand)}
.brand-name{font-weight:400;font-size:30px;letter-spacing:1px;color:var(--brand);line-height:1}
.brand-tag{font-weight:400;font-size:12px;letter-spacing:5px;color:var(--brand-sub);margin-top:6px}
.social{position:absolute;left:904px;top:47px;display:flex;gap:3px}
.social span{width:34px;height:34px;border-radius:50%;background:var(--nav-bg)}
.search{position:absolute;left:843px;top:106px;width:215px;height:35px;border:1px solid #d6d6d6;border-radius:18px;background:#f4f4f4;font-family:"Open Sans",sans-serif;font-size:12px;color:#555;padding:9px 0 0 13px}
.search-btn{position:absolute;right:0;top:0;width:34px;height:33px;border-left:1px solid #d6d6d6;border-radius:0 18px 18px 0;background:#fafafa}
.search-btn svg{position:absolute;left:10px;top:9px}

.main-nav{position:absolute;left:0;top:178px;width:1200px;height:71px;background:var(--nav-bg)}
.main-nav ul{list-style:none;position:absolute;left:126px;top:0;display:flex;height:71px}
.main-nav li{font-weight:300;font-size:19px;color:var(--nav-text);padding:23px 11px 0;height:71px;letter-spacing:.5px}
.main-nav li.is-active{background:var(--nav-active);color:var(--white);padding:23px 12px 0 15px}

.hero{position:absolute;left:0;top:249px;width:1200px;height:764px;
  background:
   radial-gradient(ellipse 380px 120px at 300px 470px,rgba(190,80,220,.55),transparent),
   radial-gradient(ellipse 300px 140px at 680px 480px,rgba(80,200,120,.45),transparent),
   radial-gradient(ellipse 320px 140px at 960px 500px,rgba(230,110,60,.5),transparent),
   radial-gradient(ellipse 700px 300px at 600px 300px,rgba(60,40,110,.6),transparent),
   linear-gradient(#0a0714,#16112a 55%,#0b0a12 80%,#050505)}
.hero-dots{position:absolute;left:972px;top:273px;display:flex;gap:5px}
.hero-dots span{width:16px;height:16px;border-radius:50%;background:var(--dot);border:2px solid #999}
.hero-dots span.is-current{background:var(--dot-active)}
.hero-title{position:absolute;left:0;top:300px;width:1217px;text-align:center;font-weight:400;font-size:46px;line-height:60px;color:var(--white);letter-spacing:.6px}
.hero-caption{position:absolute;left:101px;top:626px;width:326px;height:146px;background:linear-gradient(rgba(255,255,255,.93),rgba(235,238,242,.85));border-radius:3px}
.hero-caption p{font-family:"Open Sans",sans-serif;font-size:13.5px;letter-spacing:-.1px;line-height:18px;color:#222;padding:20px 22px 0 24px;text-align:justify}
.btn-more{position:absolute;left:101px;top:730px;width:76px;height:35px;background:#050505;color:#fff;font-size:15px;font-weight:300;padding:7px 0 0 16px;border-radius:0 4px 4px 0}

.tile{position:absolute;top:772px;width:326px;height:77px;background:linear-gradient(var(--tile-top),var(--tile-bottom));border-radius:3px}
.tile h2{font-weight:400;font-size:26px;color:var(--white);position:absolute;left:24px;top:22px}
.tile .go{position:absolute;right:14px;top:16px;width:46px;height:46px;border-radius:50%;background:#000}
.tile .go svg{position:absolute;left:12px;top:12px}
.tile--about{left:101px;border-top:6px solid var(--tile-accent)}
.tile--about h2{top:16px}.tile--about .go{top:10px}
.tile--services{left:433px}
.tile--services h2{left:29px}
.tile--services .go{right:20px}
.tile--team{left:765px}
.tile--team .go{right:20px}

.partners{position:absolute;left:104px;top:873px;width:987px;height:108px;background:var(--white);border-radius:2px}
.partners-title{position:absolute;left:30px;top:20px;font-size:24px;line-height:32px;color:var(--grey);text-align:center}
.partners-title b{font-weight:400;font-size:36px;display:block;line-height:34px}
.partners-rule{position:absolute;left:153px;top:15px;width:1px;height:80px;background:var(--line)}
.partner{position:absolute;top:38px;font-size:22px;font-weight:400;color:#666;white-space:nowrap}

.site-footer{position:absolute;left:0;top:1013px;width:1200px;height:127px;background:var(--white);border-left:1px solid #999}
.footer-nav{position:absolute;left:171px;top:35px;display:flex;font-size:13.5px;color:#333;font-weight:400;white-space:nowrap}
.footer-nav span.sep{padding:0 26px}
.copyright{position:absolute;left:0;top:62px;width:1200px;text-align:center;font-size:13.5px;color:#333}
</style>
</head>
<body>
<header class="site-header">
  <div class="brand">
    <span class="brand-mark"></span>
    <div>
      <div class="brand-name">ORVALINK</div>
      <div class="brand-tag">BUSINESS CONSULTANTS</div>
    </div>
  </div>
  <div class="social" aria-label="Social links"><span></span><span></span><span></span><span></span></div>
  <div class="search">Search...
    <div class="search-btn"><svg width="14" height="14" viewBox="0 0 14 14"><circle cx="5.5" cy="5.5" r="4.3" fill="none" stroke="#888" stroke-width="2"/><line x1="8.7" y1="8.7" x2="13" y2="13" stroke="#888" stroke-width="2.2"/></svg></div>
  </div>
</header>

<nav class="main-nav">
  <ul>
    <li class="is-active">HOME</li><li>ABOUT US</li><li>ABOUT QIANHAI</li><li>SERVICES</li><li>PORTFOLIO</li><li>PARTNERS</li><li>OUR TEAM</li><li>CONTACT US</li>
  </ul>
</nav>

<div class="hero" role="img" aria-label="Night city skyline with colourful lit towers reflected over the water"></div>
<div class="hero-dots"><span></span><span></span><span></span><span class="is-current"></span></div>
<h1 class="hero-title">QUASI ARCHITECTO BEATAE VITAE DICTA</h1>
<div class="hero-caption"><p>Sed ut perspiciatis unde omnis iste natus error sit voluptatem accusantium dolo&shy;remque laudantium, totam rem aperiam, eaque ipsa quae ab illo inventore veritatis&nbsp;et</p></div>
<div class="btn-more">MORE</div>

<div class="tile tile--about"><h2>ABOUT</h2><span class="go"><svg width="22" height="22" viewBox="0 0 22 22"><path d="M2 11h16M11 4l7 7-7 7" fill="none" stroke="#fff" stroke-width="3"/></svg></span></div>
<div class="tile tile--services"><h2>SERVICES</h2><span class="go"><svg width="22" height="22" viewBox="0 0 22 22"><path d="M2 11h16M11 4l7 7-7 7" fill="none" stroke="#fff" stroke-width="3"/></svg></span></div>
<div class="tile tile--team"><h2>OUR TEAM</h2><span class="go"><svg width="22" height="22" viewBox="0 0 22 22"><path d="M2 11h16M11 4l7 7-7 7" fill="none" stroke="#fff" stroke-width="3"/></svg></span></div>

<section class="partners">
  <div class="partners-title"><b>OUR</b>PARTNERS</div>
  <div class="partners-rule"></div>
  <div class="partner" style="left:172px">Marlowe Equity</div>
  <div class="partner" style="left:340px">Kestra Partners</div>
  <div class="partner" style="left:510px">Lunvale</div>
  <div class="partner" style="left:628px">Brisko Partners</div>
  <div class="partner" style="left:790px">Tellory Network</div>
</section>

<footer class="site-footer">
  <div class="footer-nav">
    <span>Home</span><span class="sep">|</span><span>About Us</span><span class="sep">|</span><span>About Qianhai</span><span class="sep">|</span><span>Services</span><span class="sep">|</span><span>Portfolio</span><span class="sep">|</span><span>Partners</span><span class="sep">|</span><span>Our Team</span><span class="sep">|</span><span>Contact Us</span>
  </div>
  <div class="copyright">Copyright@Harbourline Transit.example 2011. All Rights Reserved</div>
</footer>
</body>
</html>
```